Business card for Sports Apparel business

DOUBLE SIDED DESIGN
We need business cards for a new sports apparel business. We are developing a protective headband for soccer initially.
Corvell is focused on designing and developing head protection products to reduce the likelihood of concussion when playing sports. Exploring and understanding medical insights, material science research, current and former players experiences and governing bodies guidelines has allowed Corvell to develop the safety, style, form and function requirements of a suitable product to bring to market.
Target Market(s)
Mums buying kits for the sons and daughters. Amateur footballers.
Industry/Entity Type
Sporting Good
Contact Information for Business Card
Martin Ashgrove - CEO
Mobile: +44 7391608254
Email: martin@corvell.co.uk
Tel: 0208 5143927
Helena Pardoe - COO
Mob: +44 7356 409183
Email: helena@corvell.co.uk
Tel: 0208 5143927
Duncan Wyvern - CCO
Mob: +44 7468 230517
Email: duncan@corvell.co.uk
Tel: 0208 5143927
Look and feel

```html
<!DOCTYPE html>
<html lang="en">
<head>
<meta charset="utf-8">
<title>Corvell — Business Card</title>
<link href="https://fonts.googleapis.com/css2?family=Montserrat:wght@400;500;700&display=swap" rel="stylesheet">
<style>
  :root {
    --backdrop: #1b1b1b;
    --card: #2b2a29;
    --brand-blue: #1f6aa8;
    --ink-white: #ffffff;
  }
  * { margin: 0; padding: 0; box-sizing: border-box; }
  html, body {
    width: 1200px;
    height: 1021px;
    overflow: hidden;
    background: var(--backdrop);
    font-family: "Montserrat", sans-serif;
  }
  .canvas {
    position: relative;
    width: 1200px;
    height: 1021px;
  }
  .card {
    position: absolute;
    left: 250px;
    width: 700px;
    height: 400px;
    background: var(--card);
    box-shadow: 0 10px 30px rgba(0,0,0,0.55);
  }
  .card--front { top: 50px; }
  .card--back { top: 571px; }

  /* Front */
  .front-wordmark {
    position: absolute;
    left: 0; right: 0;
    top: 50%;
    transform: translateY(-50%);
    display: flex;
    align-items: center;
    justify-content: center;
    gap: 18px;
  }
  .wordmark-square {
    width: 22px;
    height: 22px;
    background: var(--brand-blue);
  }
  .wordmark-name {
    color: var(--ink-white);
    font-weight: 700;
    font-size: 60px;
    letter-spacing: 4px;
    text-transform: uppercase;
  }

  /* Back */
  .back-wordmark {
    position: absolute;
    left: 70px;
    top: 40px;
    width: 60px;
    height: 320px;
    display: flex;
    align-items: center;
    justify-content: center;
  }
  .back-wordmark .wordmark-name {
    font-size: 46px;
    letter-spacing: 3px;
    transform: rotate(90deg);
    white-space: nowrap;
  }
  .person {
    position: absolute;
    left: 400px;
    top: 150px;
  }
  .person-name {
    color: var(--brand-blue);
    font-weight: 700;
    font-size: 20px;
    letter-spacing: 0.3px;
  }
  .person-role {
    color: var(--ink-white);
    font-weight: 400;
    font-size: 14px;
    margin-top: 2px;
  }
  .contact-list {
    position: absolute;
    left: 400px;
    top: 262px;
    list-style: none;
  }
  .contact-item {
    display: flex;
    align-items: center;
    gap: 10px;
    color: var(--ink-white);
    font-size: 16px;
    font-weight: 500;
    line-height: 26px;
  }
  .contact-icon {
    width: 15px;
    height: 15px;
    flex: none;
  }
</style>
</head>
<body>
<main class="canvas">

  <section class="card card--front" aria-label="Card front">
    <div class="front-wordmark">
      <span class="wordmark-square"></span>
      <span class="wordmark-name">Corvell</span>
    </div>
  </section>

  <section class="card card--back" aria-label="Card back">
    <div class="back-wordmark">
      <span class="wordmark-name">Corvell</span>
    </div>

    <div class="person">
      <p class="person-name">Martin Ashgrove</p>
      <p class="person-role">CEO</p>
    </div>

    <ul class="contact-list">
      <li class="contact-item">
        <svg class="contact-icon" viewBox="0 0 16 16" fill="none" stroke="#1f6aa8" stroke-width="1.4">
          <rect x="4" y="1" width="8" height="14" rx="1.5"/>
          <line x1="7" y1="12.5" x2="9" y2="12.5"/>
        </svg>
        <span>+44 7391608254</span>
      </li>
      <li class="contact-item">
        <svg class="contact-icon" viewBox="0 0 16 16">
          <path fill="#1f6aa8" d="M3.6 1.2l2.3 2.6-1.2 1.7c.9 2 2.6 3.8 4.6 4.7l1.7-1.2 2.6 2.3-1.4 2.6C7.4 13.6 2.3 8.6 1.2 3.1z"/>
        </svg>
        <span>0208 5143927</span>
      </li>
      <li class="contact-item">
        <svg class="contact-icon" viewBox="0 0 16 16" fill="none" stroke="#1f6aa8" stroke-width="1.4">
          <rect x="1" y="3.5" width="14" height="9"/>
          <polyline points="1,3.5 8,9 15,3.5"/>
        </svg>
        <span>martin@corvell.co.uk</span>
      </li>
      <li class="contact-item">
        <svg class="contact-icon" viewBox="0 0 16 16" fill="none" stroke="#1f6aa8" stroke-width="1.2">
          <circle cx="8" cy="8" r="6.5"/>
          <ellipse cx="8" cy="8" rx="3" ry="6.5"/>
          <line x1="1.5" y1="8" x2="14.5" y2="8"/>
        </svg>
        <span>www.corvell.co.uk</span>
      </li>
    </ul>
  </section>

</main>
</body>
</html>
```